Christmas social media advert post

I am looking for an eye catching advert for use mainly on social media posts.
The following is the detail of the event.

Christmas special offer-
£10pp,– offer includes –
Half an hour Toboggan track,
Half an hour Slingshot paintballs (20 paintballs pp) and safe target archery (under cover and indoor ranges). Activities all the family from age 4 to grandparents can join in,
Also available – Add on indoor activities including Mini Curling, Zap Blitz, Safe axe throwing, Air juggler – from £3.50pp and age 6plus
Café open for hot food and drinks in the ‘Snug Holly Lodge and the heated Christmas marquee.

A basic idea I put together for what I feel is the important information is -

Christmas Special offer -
Starts Saturday 20th December.
£10pp – offer includes –
Half an hour Slingshot paintballs (20 paintballs pp) and safe target archery (under cover and indoor ranges). Activities all the family from age 4 to grandparents can join in. Booking is essential - details on how below.
Also available Add on indoor activities - including Mini Curling, Zap Blitz, Safe axe throwing, Air juggler – from £3.50pp and age 6plus.
Ages start from 4 plus.
All activities are great for children and adults so perfect for families as well as friends, parties and get togethers.
Free huge car parks,
Booking is easy-
Just Message from messenger (on this post) or email
colin@bluefernleisurepark.co.uk for availability of your preferred date and time.

I would be happy to send the detailed information to enquiries if it meant a better looking advert / post.

Full details are in the picture uploads, feel free to use as much or as little of the information as you feel best.

```html
<!DOCTYPE html>
<html lang="en">
<head>
<meta charset="utf-8">
<title>Christmas Special Offer</title>
<link rel="stylesheet" href="https://fonts.googleapis.com/css2?family=Oswald:wght@400;700&family=Great+Vibes&family=Poppins:wght@400;500;600;700;800&family=EB+Garamond:ital@1&family=Merriweather:wght@700&display=swap">
<style>
:root{
  --backdrop:#262626;
  --red:#d0121f;
  --red-deep:#a70a1b;
  --red-bright:#e61d27;
  --gold:#f7bf22;
  --gold-deep:#e4a317;
  --ink:#1c1c1c;
  --white:#ffffff;
  --snow:#dfeef6;
  --orange:#ff4b12;
  --text-red:#c1121f;
  --cafe-red:#a3111f;
}
*{margin:0;padding:0;box-sizing:border-box}
html,body{width:995px;height:1200px;overflow:hidden;background:var(--backdrop)}
.poster{position:absolute;left:88px;top:78px;width:818px;height:1059px;background:var(--white);overflow:hidden;font-family:"Poppins",sans-serif;color:var(--ink)}
.hero-band{position:absolute;left:0;top:0;width:818px;height:560px}
.ornaments{position:absolute;left:394px;top:0;width:424px;height:124px;background:radial-gradient(ellipse at 50% 40%,rgba(247,191,34,.35),rgba(247,191,34,0) 70%)}
.date-badge{position:absolute;left:45px;top:0;width:183px;height:196px;background:var(--gold);border-radius:0 0 62px 62px;box-shadow:0 6px 12px rgba(0,0,0,.18);text-align:center;padding-top:22px;font-family:"Oswald",sans-serif;font-size:31px;line-height:34px;letter-spacing:-.3px;text-transform:uppercase;color:var(--ink)}
.date-badge .light{font-weight:400}
.date-badge .strong{font-weight:700}
.title-script{position:absolute;left:230px;top:112px;width:420px;text-align:center;font-family:"Great Vibes",cursive;font-size:102px;line-height:1;color:var(--white)}
.title-main{position:absolute;left:200px;top:205px;width:476px;text-align:center;font-weight:700;font-size:56px;letter-spacing:1px;line-height:1.2;color:var(--white)}
.photo{position:absolute;border-radius:50%;background:var(--red);display:flex;align-items:center;justify-content:center}
.photo span{display:block;border-radius:50%}
.photo-left{left:89px;top:282px;width:184px;height:184px}
.photo-left span{width:166px;height:166px;background:linear-gradient(160deg,#3a3f58,#5a4a6a 50%,#3b3b3b)}
.photo-centre{left:278px;top:281px;width:250px;height:250px}
.photo-centre span{width:236px;height:236px;background:linear-gradient(160deg,#8a928a,#4b5f9c 40%,#b8454a 65%,#7e817a)}
.photo-right{left:538px;top:282px;width:184px;height:184px}
.photo-right span{width:166px;height:166px;background:linear-gradient(180deg,#a8b59c,#c9ad88 40%,#d6c2a4)}
.pill{position:absolute;height:43px;border-radius:22px;background:linear-gradient(90deg,var(--red-deep),var(--red-bright));color:var(--white);font-weight:700;font-size:22px;line-height:43px;padding-left:23px}
.pill-offer{left:61px;top:553px;width:285px}
.pill-extra{left:422px;top:553px;width:285px}
.pill-juggler{left:422px;top:660px;width:285px}
.list{position:absolute;list-style:none;font-size:16px;line-height:19.4px;color:var(--ink);white-space:nowrap}
.list li{position:relative;padding-left:21px;margin-bottom:6px}
.list li svg{position:absolute;left:0;top:3px;width:14px;height:14px}
.list-offer{left:82px;top:607px;width:340px}
.list-extra{left:444px;top:607px;width:340px}
.list-juggler{left:444px;top:714px;width:300px}
.list-juggler li{padding-left:25px}
.rule{position:absolute;left:55px;width:709px;height:1px;background:var(--text-red);opacity:.6}
.rule-top{top:765px}
.rule-bottom{top:824px}
.cafe-note{position:absolute;left:60px;top:768px;width:700px;text-align:center;font-family:"EB Garamond",serif;font-style:italic;font-size:21px;line-height:24px;color:var(--cafe-red)}
.snow-field{position:absolute;left:0;top:825px;width:818px;height:234px;background:linear-gradient(180deg,#eaf3f8,var(--snow) 50%,#f4f8fb)}
.winter-scene{position:absolute;left:0;top:906px;width:818px;height:153px;background:linear-gradient(180deg,rgba(255,255,255,0),rgba(255,255,255,.85) 55%,rgba(120,170,90,.45))}
.booking-pill{position:absolute;left:58px;top:843px;width:222px;height:38px;border-radius:19px;background:linear-gradient(90deg,var(--orange),var(--red-bright));color:var(--white);font-weight:500;font-size:20.5px;line-height:38px;text-align:center;letter-spacing:.3px}
.booking-copy{position:absolute;font-family:"Merriweather",serif;font-weight:700;font-size:13.2px;line-height:18.5px;color:var(--ink);white-space:nowrap}
.booking-lead{left:291px;top:843px}
.booking-lead .email{color:var(--text-red)}
.booking-tail{left:195px;top:886px}
.car-parks{position:absolute;left:657px;top:845px;display:flex;align-items:center;gap:7px;color:var(--text-red);font-weight:600;font-size:15px;line-height:15px}
.car-parks svg{width:27px;height:27px}
</style>
</head>
<body>
<main class="poster">
  <svg class="hero-band" viewBox="0 0 818 560" aria-hidden="true">
    <defs>
      <linearGradient id="heroRed" x1="0" y1="0" x2="1" y2="1">
        <stop offset="0" stop-color="#d8131f"/>
        <stop offset=".55" stop-color="#c70f1e"/>
        <stop offset="1" stop-color="#b00c1c"/>
      </linearGradient>
      <linearGradient id="swoosh" x1="0" x2="1">
        <stop offset="0" stop-color="#f6c12a"/>
        <stop offset="1" stop-color="#e4a317"/>
      </linearGradient>
    </defs>
    <path d="M0 339 Q409 520 818 339 L818 380 Q409 555 0 352 Z" fill="url(#swoosh)"/>
    <path d="M0 0 H818 V334 Q409 505 0 334 Z" fill="url(#heroRed)"/>
    <path d="M0 345 Q409 520 818 345 L818 352 Q409 528 0 356 Z" fill="#ffffff"/>
  </svg>

  <div class="ornaments" role="img" aria-label="Hanging gold Christmas baubles, stars, snowflakes, a reindeer and fairy lights"></div>

  <div class="date-badge">
    <div class="light">Starts</div>
    <div class="light">Saturday</div>
    <div class="strong">20th</div>
    <div class="strong">December</div>
  </div>

  <h1>
    <span class="title-script">Christmas</span>
    <span class="title-main">SPECIAL OFFER</span>
  </h1>

  <div class="photo photo-left"><span role="img" aria-label="Photo of a player aiming a slingshot paintball in a neon-lit range"></span></div>
  <div class="photo photo-centre"><span role="img" aria-label="Photo of safe throwing axes stuck in a bristle target"></span></div>
  <div class="photo photo-right"><span role="img" aria-label="Photo of a player sliding a stone on an indoor mini curling lane"></span></div>

  <div class="pill pill-offer">£10pp– offer includes</div>
  <ul class="list list-offer">
    <li><svg viewBox="0 0 14 14"><g stroke="#e8a91c" stroke-width="2" stroke-linecap="round"><path d="M7 1v12M1 7h12M2.8 2.8l8.4 8.4M11.2 2.8l-8.4 8.4"/></g></svg>Half an hour Toboggan track</li>
    <li><svg viewBox="0 0 14 14"><g stroke="#e8a91c" stroke-width="2" stroke-linecap="round"><path d="M7 1v12M1 7h12M2.8 2.8l8.4 8.4M11.2 2.8l-8.4 8.4"/></g></svg>Half an hour Slingshot paintballs<br>(20 paintballs pp) and safe target<br>archery (under cover and<br>indoor ranges). Activities all the<br>family from age 4 to grandparents<br>can join in,</li>
  </ul>

  <div class="pill pill-extra">Also available</div>
  <ul class="list list-extra">
    <li><svg viewBox="0 0 14 14"><g stroke="#e8a91c" stroke-width="2" stroke-linecap="round"><path d="M7 1v12M1 7h12M2.8 2.8l8.4 8.4M11.2 2.8l-8.4 8.4"/></g></svg>Add on indoor activities including Mini<br>Curling, Zap Blitz, Safe axe throwing,</li>
  </ul>

  <div class="pill pill-juggler">Air juggler</div>
  <ul class="list list-juggler">
    <li><svg viewBox="0 0 14 14"><g stroke="#e8a91c" stroke-width="2" stroke-linecap="round"><path d="M7 1v12M1 7h12M2.8 2.8l8.4 8.4M11.2 2.8l-8.4 8.4"/></g></svg>from £3.50pp and age 6plus</li>
  </ul>

  <div class="snow-field"></div>
  <div class="rule rule-top"></div>
  <p class="cafe-note">Café open for hot food and drinks in the ‘Snug Holly Lodge and the<br>heated Christmas marquee.</p>
  <div class="rule rule-bottom"></div>

  <div class="booking-pill">BOOKING IS EASY</div>
  <p class="booking-copy booking-lead">Just Message from messenger (on this post) or<br>email <span class="email">colin@bluefernleisurepark.co.uk</span></p>
  <p class="booking-copy booking-tail">for availability of your preferred date and time.</p>

  <div class="car-parks">
    <svg viewBox="0 0 27 27" fill="none" stroke="#c1121f" stroke-width="1.6">
      <rect x="2" y="2" width="23" height="23" rx="2"/>
      <path d="M2 13.5h23"/>
      <path d="M6 10l1.5-4h7l1.5 4z"/><path d="M11 23l1.5-4h7l1.5 4z"/>
    </svg>
    <span>FREE HUGE<br>CAR PARKS</span>
  </div>

  <div class="winter-scene" role="img" aria-label="Snowy hillside with pine cones, a frosted pink bauble and pine needles"></div>
</main>
</body>
</html>
```